Brivond Technologies business card design

We need a business card designed with our new logo. it would be great if the card could communicate it is a technology based company.

Target Market(s)

system integrators

Industry/Entity Type

technology, IOT

Contact Information for Business Card

Name, designation, Address, telephone number, email address

Requirements
Must have
• logo and company name
Nice to have
• something to do with technology

```html
<!DOCTYPE html>
<html lang="en">
<head>
<meta charset="utf-8">
<title>Brivond Technologies – Business Card</title>
<link href="https://fonts.googleapis.com/css2?family=Open+Sans:wght@400;600;700&display=swap" rel="stylesheet">
<style>
  :root {
    --backdrop: #3b3b3b;
    --card-white: #ffffff;
    --card-black: #141414;
    --ink-dark: #3a3a3a;
    --ink-grey: #555555;
    --accent: #f7931e;
    --ink-light: #ffffff;
  }
  * { box-sizing: border-box; margin: 0; padding: 0; }
  html, body {
    width: 1200px; height: 801px; overflow: hidden;
    background: var(--backdrop);
    font-family: "Open Sans", Arial, sans-serif;
  }
  .stage {
    width: 1200px; height: 801px;
    display: flex; align-items: center; justify-content: center; gap: 40px;
  }
  .card {
    position: relative;
    width: 540px; height: 309px;
    border-bottom: 3px solid var(--accent);
    box-shadow: 0 10px 30px rgba(0,0,0,.35);
    overflow: hidden;
  }
  /* Front */
  .card-front { background: var(--card-white); }
  .front-brand {
    position: absolute; left: 30px; top: 50%; transform: translateY(-50%);
    width: 250px;
    display: flex; align-items: center; gap: 9px;
    white-space: nowrap;
  }
  .brand-square { width: 15px; height: 15px; background: var(--accent); flex: none; }
  .front-brand .brand-name {
    font-weight: 700; font-size: 18px; color: var(--ink-dark); letter-spacing: .3px;
  }
  .divider {
    position: absolute; left: 300px; top: 60px; bottom: 60px;
    width: 1.5px; background: var(--accent);
  }
  .contact {
    position: absolute; left: 318px; top: 62px; right: 16px;
    color: var(--ink-grey); font-size: 12.5px; line-height: 1.55;
    white-space: nowrap;
  }
  .contact .person-name {
    color: var(--accent); font-weight: 700; font-size: 17px; line-height: 1.2;
  }
  .contact .person-role { margin-bottom: 10px; }
  .contact .address { margin-bottom: 10px; }
  .contact-line { display: flex; align-items: center; gap: 7px; }
  .contact-line svg { width: 11px; height: 11px; flex: none; fill: var(--accent); }
  /* Back */
  .card-back {
    background: radial-gradient(ellipse at 30% 60%, #262626 0%, var(--card-black) 60%);
  }
  .back-brand {
    position: absolute; right: 40px; bottom: 70px;
    display: flex; align-items: center; gap: 12px;
    white-space: nowrap;
  }
  .back-brand .brand-name {
    font-weight: 700; font-size: 26px; color: var(--ink-light); letter-spacing: .5px;
  }
</style>
</head>
<body>
<main class="stage">
  <section class="card card-front" aria-label="Business card front">
    <div class="front-brand">
      <span class="brand-square"></span>
      <span class="brand-name">Brivond Technologies</span>
    </div>
    <div class="divider"></div>
    <div class="contact">
      <div class="person-name">DALE HARKER</div>
      <div class="person-role">President</div>
      <div class="address">3170 Coral Ridge Drive<br>Seaview CA 92014</div>
      <div class="contact-line">
        <svg viewBox="0 0 24 24"><path d="M6.6 10.8a15 15 0 0 0 6.6 6.6l2.2-2.2a1 1 0 0 1 1-.25 11.4 11.4 0 0 0 3.6.57 1 1 0 0 1 1 1V20a1 1 0 0 1-1 1A17 17 0 0 1 3 4a1 1 0 0 1 1-1h3.5a1 1 0 0 1 1 1c0 1.25.2 2.45.57 3.6a1 1 0 0 1-.25 1z"/></svg>
        <span>555-014-2280</span>
      </div>
      <div class="contact-line">
        <svg viewBox="0 0 24 24"><path d="M2 5h20v14H2z M2 5l10 8 10-8" /></svg>
        <span>info@brivondtech.com</span>
      </div>
      <div class="contact-line">
        <svg viewBox="0 0 24 24"><circle cx="12" cy="12" r="10"/></svg>
        <span>www.brivondtech.com</span>
      </div>
    </div>
  </section>

  <section class="card card-back" aria-label="Business card back">
    <div class="back-brand">
      <span class="brand-square"></span>
      <span class="brand-name">Brivond Technologies</span>
    </div>
  </section>
</main>
</body>
</html>
```